Energy trading company (Voltarix) needs a business card

We need a business card for a company based in Central America. Our main purpose is trading energy . We already have the logo but we need some good creativity to design a high impact business card. Colors blue, orange, green can be used or we would like to see good combinatios with our logo

Target Market(s)

Energy

Industry/Entity Type

Power Generation

Contact Information for Business Card

Logo , headquarters , name, background

Font styles to use
Serif
Sans Serif

Colors

Designer to choose colors to be used in the design.

Requirements
Must have
• it must have a fresh and clean view
Nice to have
• good backgrounds that combine with the logo
Should not have
• too much words

```html
<!DOCTYPE html>
<html lang="en">
<head>
<meta charset="utf-8">
<title>Voltarix Business Card</title>
<link rel="stylesheet" href="https://fonts.googleapis.com/css2?family=Tinos:wght@400;700&display=swap">
<style>
  :root {
    --page: #c9c9c9;
    --card: #0b0b0d;
    --card-soft: #131315;
    --orange: #f5841f;
    --white: #ffffff;
  }
  * { box-sizing: border-box; margin: 0; padding: 0; }
  html, body {
    width: 1125px; height: 1200px; overflow: hidden;
    background: var(--page);
  }
  .canvas {
    position: relative; width: 1125px; height: 1200px;
  }
  .card {
    position: absolute; left: 112px; width: 900px; height: 511px;
    background: var(--card); border-radius: 24px; overflow: hidden;
    box-shadow: 0 4px 10px rgba(0,0,0,0.25);
    font-family: "Tinos", "Times New Roman", serif;
    text-align: center;
  }
  .card--front { top: 60px; }
  .card--back { top: 630px; }
  .card__decor { position: absolute; }
  .card--front .card__decor { right: -230px; top: 15px; width: 480px; height: 480px; }
  .card--back .card__decor { left: -250px; top: 10px; width: 500px; height: 500px; }
  .brand {
    position: absolute; left: 0; right: 0;
    display: flex; flex-direction: column; align-items: center;
  }
  .brand__dot {
    border-radius: 50%; background: var(--orange);
  }
  .brand__name {
    font-family: "Tinos", "Times New Roman", serif; font-weight: 700;
    color: var(--orange); letter-spacing: 2px; line-height: 1;
  }
  .card--front .brand { top: 66px; gap: 22px; }
  .card--front .brand__dot { width: 56px; height: 56px; }
  .card--front .brand__name { font-size: 60px; }
  .card--back .brand { top: 150px; gap: 28px; }
  .card--back .brand__dot { width: 80px; height: 80px; }
  .card--back .brand__name { font-size: 84px; }
  .person {
    position: absolute; left: 0; right: 0; top: 256px;
  }
  .person__name {
    color: var(--orange); font-weight: 700; font-size: 30px; letter-spacing: 1px;
  }
  .person__role {
    color: var(--white); font-size: 19px; margin-top: 6px;
  }
  .person__rule {
    width: 38px; height: 2px; background: var(--orange); margin: 14px auto 0;
  }
  .contact-icons {
    position: absolute; left: 0; right: 0; top: 352px;
    display: flex; justify-content: center; gap: 7px;
  }
  .contact-icons svg { width: 22px; height: 22px; }
  .contact {
    position: absolute; left: 0; right: 0; top: 386px;
    color: var(--white); font-size: 19px; line-height: 29px; letter-spacing: 0.3px;
  }
</style>
</head>
<body>
<div class="canvas">
  <section class="card card--front">
    <svg class="card__decor" viewBox="0 0 480 480" aria-hidden="true">
      <circle cx="240" cy="240" r="205" fill="none" stroke="var(--card-soft)" stroke-width="60"/>
    </svg>
    <div class="brand">
      <span class="brand__dot"></span>
      <span class="brand__name">VOLTARIX</span>
    </div>
    <div class="person">
      <div class="person__name">MARCO REYES</div>
      <div class="person__role">Owner</div>
      <div class="person__rule"></div>
    </div>
    <div class="contact-icons">
      <svg viewBox="0 0 22 22" aria-label="Phone">
        <circle cx="11" cy="11" r="11" fill="var(--orange)"/>
        <path d="M7 6.5l2 0 1 2.5-1.3 1a6 6 0 0 0 3 3l1-1.3 2.5 1v2c-5 .5-9-3.5-8.2-8.2z" fill="var(--card)"/>
      </svg>
      <svg viewBox="0 0 22 22" aria-label="Email">
        <circle cx="11" cy="11" r="11" fill="var(--orange)"/>
        <rect x="5.5" y="7" width="11" height="8" rx="1" fill="none" stroke="var(--card)" stroke-width="1.4"/>
        <path d="M6 7.5l5 4 5-4" fill="none" stroke="var(--card)" stroke-width="1.4"/>
      </svg>
      <svg viewBox="0 0 22 22" aria-label="Website">
        <circle cx="11" cy="11" r="11" fill="var(--orange)"/>
        <circle cx="11" cy="11" r="6" fill="none" stroke="var(--card)" stroke-width="1.4"/>
        <path d="M5 11h12M11 5c-3 3.5-3 8.5 0 12M11 5c3 3.5 3 8.5 0 12" fill="none" stroke="var(--card)" stroke-width="1.1"/>
      </svg>
    </div>
    <div class="contact">
      <div>(555) 014-2290</div>
      <div>info@voltarix.com</div>
      <div>www.voltarix.com</div>
    </div>
  </section>

  <section class="card card--back">
    <svg class="card__decor" viewBox="0 0 500 500" aria-hidden="true">
      <circle cx="250" cy="250" r="210" fill="none" stroke="var(--card-soft)" stroke-width="70"/>
    </svg>
    <div class="brand">
      <span class="brand__dot"></span>
      <span class="brand__name">VOLTARIX</span>
    </div>
  </section>
</div>
</body>
</html>
```